Off Campus Housing website service for universities needs corporate brochure

We need a corporate brochure targeted at universities to get them to partner with us to offer an Off-Campus Housing website with housing listings and educational resources for their students. We provide hosted software and support, off-campus housing listings, and educational resources to embed in the university website (i.e http://rentalhub.brx.edu); the university promotes the service to off-campus students, parents, and faculty/staff. We have a dedicated account executive to work with each university to promote the website to property managers in the schools area who pay to list their properties on the site. We currently partner with over 100 colleges and universities across the country to serve the needs of their off-campus students. Our corporate website is: www.lodgebridgealliance.com.
Updates

Target Market(s)

Universities and Colleges

Industry/Entity Type

Marketing

Font styles to use
Serif

Requirements
Must have
• Our logo
• Our website (www.lodgebridgealliance.com)
• Contact information (this is different than what we used on our previous brochure, image attached):
• Email: sales@lodgebridgealliance.com
• Student image(s) - must be diverse
• Phone: 866-402-7719
Nice to have
• University/Campus image (generic)

```html
<!DOCTYPE html>
<html lang="en">
<head>
<meta charset="utf-8">
<title>Lodgebridge Alliance – University Partner Brochure</title>
<link href="https://fonts.googleapis.com/css2?family=Open+Sans:ital,wght@0,400;0,600;0,700;0,800;1,400;1,600;1,700&display=swap" rel="stylesheet">
<style>
  :root {
    --blue: #0a5bc4;
    --blue-dark: #0646a0;
    --blue-light: #2f7de0;
    --ink: #1c1c1c;
    --paper: #ffffff;
    --paper-shade: #eef0f3;
    --stage: #e6e7e9;
    --photo-warm: #c9704a;
    --photo-red: #b8303c;
    --photo-autumn: #d9962e;
  }
  * { box-sizing: border-box; margin: 0; padding: 0; }
  html, body { width: 1200px; height: 1200px; overflow: hidden; }
  body {
    background: radial-gradient(circle at 50% 45%, #f6f6f7 0%, var(--stage) 75%);
    font-family: "Open Sans", Arial, sans-serif;
    color: var(--ink);
  }
  .spread {
    position: absolute; left: 50px; top: 210px;
    width: 1100px; height: 780px;
    display: flex;
    box-shadow: 0 18px 40px rgba(0,0,0,.18);
  }
  .page { position: relative; width: 550px; height: 780px; background: var(--paper); overflow: hidden; }
  .page-back { background: linear-gradient(180deg, var(--paper) 0%, var(--paper-shade) 100%); }
  .page svg.page-art { position: absolute; inset: 0; }

  /* back page */
  .audience { position: absolute; left: 60px; width: 420px; }
  .audience h3 { color: var(--blue); font-size: 15px; font-weight: 700; font-style: italic; text-transform: uppercase; }
  .audience p { font-size: 13px; font-style: italic; line-height: 1.35; }
  .audience-students { top: 44px; }
  .audience-university { top: 120px; }
  .intro-photo {
    position: absolute; left: 60px; top: 215px; width: 410px; height: 150px;
    border: 3px solid var(--blue);
    background: linear-gradient(100deg, var(--photo-autumn) 0%, var(--photo-warm) 40%, #7a4a3a 70%, #3d5a3a 100%);
  }
  .partner-stats { position: absolute; left: 60px; top: 400px; width: 410px; font-size: 13.5px; font-style: italic; line-height: 1.38; }
  .contact { position: absolute; left: 60px; top: 600px; color: #fff; }
  .contact h2 { font-size: 30px; font-weight: 700; font-style: italic; text-decoration: underline; text-underline-offset: 5px; margin-bottom: 12px; }
  .contact p { font-size: 18px; font-style: italic; line-height: 1.3; }

  /* cover */
  .brand { position: absolute; left: 40px; top: 420px; width: 490px; display: flex; justify-content: center; align-items: center; gap: 10px; }
  .brand-mark { width: 22px; height: 22px; background: var(--blue); flex: none; }
  .brand-name { font-size: 24px; font-weight: 700; color: var(--blue); letter-spacing: 2px; text-transform: uppercase; white-space: nowrap; }
  .headline { position: absolute; left: 40px; top: 485px; width: 490px; text-align: center; }
  .headline h1 { color: var(--blue); font-size: 36px; font-weight: 800; line-height: 1.1; }
  .headline p { font-size: 27px; font-weight: 400; text-transform: uppercase; }
  .cover-url { position: absolute; left: 40px; top: 592px; width: 490px; text-align: center; font-size: 16px; letter-spacing: 2.5px; }
</style>
</head>
<body>
<main class="spread">
  <section class="page page-back">
    <svg class="page-art" width="550" height="780" viewBox="0 0 550 780">
      <path d="M0,560 Q250,470 550,590 L550,780 L0,780 Z" fill="#d4d8de"/>
      <path d="M0,575 Q250,488 550,605 L550,780 L0,780 Z" fill="var(--blue)"/>
      <path d="M550,40 Q470,380 520,780" fill="none" stroke="var(--blue)" stroke-width="12"/>
    </svg>
    <div class="audience audience-students">
      <h3>For your students</h3>
      <p>a single site to find off-campus housing, sublets, roommates, furniture, and education about off-campus living.</p>
    </div>
    <div class="audience audience-university">
      <h3>For your university</h3>
      <p>for your university, a custom off-campus housing program designed to meet the specific needs of your institution's campus environment.</p>
    </div>
    <div class="intro-photo" role="img" aria-label="Group of diverse smiling students outdoors among autumn trees"></div>
    <p class="partner-stats">We work with over 85 university partners, 1.4 million off-campus students, and offer a variety of funding models to suit your university's unique needs. Funding models may include potential revenue sharing.</p>
    <div class="contact">
      <h2>CONTACT US</h2>
      <p>Email: sales@lodgebridgealliance.com</p>
      <p>Phone: 866-402-7719</p>
      <p>www.lodgebridgealliance.com</p>
    </div>
  </section>

  <section class="page page-cover">
    <svg class="page-art" width="550" height="780" viewBox="0 0 550 780">
      <defs>
        <linearGradient id="groupTones" x1="0" y1="0" x2="1" y2="1">
          <stop offset="0" stop-color="#e8d6c8"/>
          <stop offset=".45" stop-color="var(--photo-warm)"/>
          <stop offset=".75" stop-color="var(--photo-red)"/>
          <stop offset="1" stop-color="#3a2a28"/>
        </linearGradient>
      </defs>
      <path d="M70,0 Q0,380 20,780" fill="none" stroke="var(--blue)" stroke-width="14"/>
      <circle cx="385" cy="60" r="312" fill="none" stroke="var(--blue)" stroke-width="12"/>
      <circle cx="385" cy="60" r="296" fill="url(#groupTones)" role="img" aria-label="Close group portrait of diverse smiling college students"/>
      <path d="M0,720 Q300,700 550,745 L550,780 L0,780 Z" fill="var(--blue)"/>
    </svg>
    <div class="brand">
      <span class="brand-mark"></span>
      <span class="brand-name">Lodgebridge Alliance</span>
    </div>
    <div class="headline">
      <h1>OFF CAMPUS HOUSING</h1>
      <p>At your students fingertips</p>
    </div>
    <p class="cover-url">www.lodgebridgealliance.com</p>
  </section>
</main>
</body>
</html>
```